Anzeigengestaltung für Bernhardinerzucht
Unkomplizierte Zusammenarbeit, der erste Entwurf hat bis auf kleine Änderungswünsche sofort gefallen.
Zielgruppe
Ich bin neu in der Bernhardinerzucht und möchte auf mich aufmerksam machen. Wir haben Anfang März unseren ersten A - Wurf Bernhardiner bekommen.
Unsere Zielgruppe sind interessierte Käufer der Rasse und andere Züchter.
Aufgabenstellung
Wir haben hübsche Welpen aus der Verpaarung von :
Rüde:
Bruno vom Haldenmoor
Hündin :
Elsa-Mai vom Haldenfeld
Die drei Rüden wurden am 6. März geboren. Sie sind Mitte Mai geimpft, mehrfach entwurmt und gechipt abgabebereit.
Kurze Beschreibung
Wir sind eine kleine Zuchtstätte.
Unser Ziel ist es, mit viel Liebe wesensfeste, gesunde und möglichst langlebige Bernhardiner
zu züchten.
Format DIN A6 ist eine halbe Seite eines Zuchtkatalog für eine Spezialzuchtschau Bernhardiner
Bitte bei den Bildern möglichst nur den Oberkörper/Kopf verwenden. Es sind zwei Bilder der Hündin und ein Bild des Rüden (Bruno vom Haldenmoor) verfügbar.

```html
<!DOCTYPE html>
<html lang="de">
<head>
<meta charset="utf-8">
<title>Bernhardiner-Welpen suchen ein Zuhause</title>
<link rel="stylesheet" href="https://fonts.googleapis.com/css2?family=Bree+Serif&family=Open+Sans:wght@400;600&display=swap">
<style>
  :root {
    --orange: #c4732f;
    --orange-light: #d98b43;
    --dark: #3d3735;
    --white: #ffffff;
    --cream: #f6f1ec;
    --text-dark: #3a302b;
    --fur-light: #e9dcd0;
  }
  * { box-sizing: border-box; margin: 0; padding: 0; }
  html, body { width: 1200px; height: 851px; overflow: hidden; background: var(--white); }
  .ad {
    position: relative;
    width: 1200px;
    height: 851px;
    overflow: hidden;
    font-family: "Open Sans", sans-serif;
    background: var(--white);
  }
  .backdrop { position: absolute; inset: 0; }
  .headline {
    position: absolute;
    left: 28px;
    top: 22px;
    color: var(--white);
    font-family: "Bree Serif", serif;
    font-weight: 400;
    line-height: 1.12;
  }
  .headline__main { display: block; font-size: 56px; }
  .headline__sub { display: block; font-size: 45px; }
  .litter-badge {
    position: absolute;
    left: 670px;
    top: 52px;
    width: 158px;
    height: 158px;
    border-radius: 50%;
    background: var(--dark);
    border: 3px solid var(--orange-light);
    color: var(--white);
    font-family: "Bree Serif", serif;
    font-size: 34px;
    line-height: 1.1;
    text-align: center;
    display: flex;
    flex-direction: column;
    justify-content: center;
    transform: rotate(-6deg);
  }
  .puppy-icons {
    position: absolute;
    left: 906px;
    top: 14px;
    width: 247px;
    height: 66px;
    border-radius: 10px;
    background: linear-gradient(90deg, var(--fur-light), #d9b28c);
    opacity: .85;
  }
  .facts {
    position: absolute;
    left: 30px;
    top: 210px;
    list-style: none;
    color: var(--text-dark);
    font-family: "Bree Serif", serif;
    font-size: 32px;
    line-height: 1.42;
  }
  .facts li::before { content: "• "; }
  .facts__note {
    display: block;
    font-family: "Open Sans", sans-serif;
    font-weight: 600;
    font-size: 19px;
    line-height: 1.1;
    padding-left: 22px;
  }
  .parent-photo {
    position: absolute;
    border-radius: 50%;
    border: 8px solid var(--orange);
  }
  .parent-photo--sire { left: 86px; top: 467px; width: 232px; height: 232px; background: radial-gradient(circle at 50% 45%, #7a4a2e, #3f2a20 55%, #e6e6ea 90%); }
  .parent-photo--dam { left: 360px; top: 468px; width: 244px; height: 244px; background: radial-gradient(circle at 50% 45%, #8d5430, #5a3a26 50%, #b9a58c 90%); }
  .parent-label {
    position: absolute;
    width: 148px;
    height: 148px;
    border-radius: 50%;
    background: var(--dark);
    border: 4px solid var(--orange);
    color: var(--white);
    text-align: center;
    display: flex;
    flex-direction: column;
    justify-content: center;
    font-size: 18px;
    line-height: 1.2;
    padding: 0 4px;
  }
  .parent-label strong { font-weight: 600; font-size: 18px; line-height: 1.25; }
  .parent-label--sire { left: 48px; top: 390px; }
  .parent-label--dam { left: 313px; top: 368px; }
  .kennel-claim {
    position: absolute;
    left: 22px;
    top: 748px;
    color: var(--white);
    font-weight: 600;
    font-size: 21.5px;
    line-height: 1.36;
  }
  .divider {
    position: absolute;
    left: 626px;
    top: 668px;
    width: 2px;
    height: 164px;
    background: var(--orange);
  }
  .pin-icon { position: absolute; left: 664px; top: 654px; }
  .kennel-name {
    position: absolute;
    left: 733px;
    top: 650px;
    color: var(--white);
    font-family: "Bree Serif", serif;
  }
  .kennel-name__title { display: block; font-size: 31px; }
  .kennel-name__sub { display: block; font-size: 21px; margin-top: 2px; }
  .contact {
    position: absolute;
    left: 682px;
    top: 745px;
    color: var(--white);
    font-style: normal;
    font-size: 21px;
    line-height: 1.3;
  }
  .contact__name { font-weight: 600; }
  .phone {
    position: absolute;
    left: 915px;
    top: 760px;
    color: var(--white);
    font-size: 30px;
    letter-spacing: 1px;
    display: flex;
    align-items: center;
    gap: 6px;
    white-space: nowrap;
  }
  .email {
    position: absolute;
    left: 918px;
    top: 800px;
    color: var(--white);
    font-size: 20px;
    white-space: nowrap;
  }
</style>
</head>
<body>
<main class="ad">
  <svg class="backdrop" width="1200" height="851" viewBox="0 0 1200 851">
    <defs>
      <linearGradient id="photo-fade" x1="0" y1="0" x2="1" y2="0">
        <stop offset="0" stop-color="#f3ebe4" stop-opacity="0"/>
        <stop offset="0.25" stop-color="#c99a78" stop-opacity="0.7"/>
        <stop offset="0.6" stop-color="#8a5436"/>
        <stop offset="1" stop-color="#b6805a"/>
      </linearGradient>
    </defs>
    <rect x="0" y="0" width="1200" height="851" fill="var(--cream)"/>
    <rect class="litter-photo" role="img" aria-label="Foto: Bernhardiner-Hündin liegt mit ihren drei Welpen in der Wurfkiste" x="420" y="90" width="780" height="520" fill="url(#photo-fade)"/>
    <path class="top-band" d="M0,0 H1200 V72 C950,96 600,120 360,150 C220,166 100,178 0,182 Z" fill="var(--orange)"/>
    <path class="top-band-edge" d="M0,182 C100,178 220,166 360,150 C600,120 950,96 1200,72" fill="none" stroke="var(--white)" stroke-width="3" opacity=".6"/>
    <path class="bottom-stripe" d="M0,650 C320,648 700,605 1200,578 V851 H0 Z" fill="var(--orange)"/>
    <path class="bottom-band" d="M0,700 C360,694 720,630 1200,604 V851 H0 Z" fill="var(--dark)"/>
  </svg>

  <h1 class="headline">
    <span class="headline__main">Bernhardiner-Welpen</span>
    <span class="headline__sub">suchen ein Zuhause</span>
  </h1>

  <div class="litter-badge"><span>unser</span><span>A-Wurf</span></div>
  <div class="puppy-icons" role="img" aria-label="Illustration: drei Welpenköpfe"></div>

  <ul class="facts">
    <li>Drei Rüden</li>
    <li>Geboren am 6. März 2019</li>
    <li>Abgabebereit Mitte Mai
      <span class="facts__note">(geimpf, entwurmt und gechipt)</span></li>
  </ul>

  <div class="parent-photo parent-photo--sire" role="img" aria-label="Foto: Rüde Bruno vom Haldenmoor im Schnee"></div>
  <div class="parent-photo parent-photo--dam" role="img" aria-label="Foto: Hündin Elsa-Mai vom Haldenfeld vor einem Haus"></div>

  <div class="parent-label parent-label--sire">
    <span>Rüde:</span>
    <strong>Bruno vom<br>Haldenmoor</strong>
    <span>(langhaar)</span>
  </div>
  <div class="parent-label parent-label--dam">
    <span>Hündin:</span>
    <strong>Elsa-Mai vom<br>Haldenfeld</strong>
    <span>(langhaar)</span>
  </div>

  <p class="kennel-claim">Wir sind eine kleine Zucht. Unser Ziel ist es,<br>mit viel Liebe wesensfeste gesunde und<br>möglichst langlebige Bernhardiner zu züchten.</p>

  <div class="divider"></div>

  <svg class="pin-icon" width="46" height="62" viewBox="0 0 46 62" aria-hidden="true">
    <path d="M23,2 C11,2 2,11 2,23 C2,38 23,60 23,60 C23,60 44,38 44,23 C44,11 35,2 23,2 Z" fill="var(--orange)"/>
    <g fill="var(--dark)">
      <ellipse cx="23" cy="29" rx="7" ry="6"/>
      <circle cx="14" cy="21" r="3"/>
      <circle cx="20" cy="16" r="3"/>
      <circle cx="27" cy="16" r="3"/>
      <circle cx="32" cy="21" r="3"/>
    </g>
  </svg>

  <div class="kennel-name">
    <span class="kennel-name__title">St. Bernhards-Zuchtstätte</span>
    <span class="kennel-name__sub">vom vorderen Eichenhain</span>
  </div>

  <address class="contact">
    <div class="contact__name">Merle Soltau</div>
    <div>Lindenwiesenstr. 14</div>
    <div>36999 Birkental</div>
  </address>

  <div class="phone">
    <svg width="26" height="26" viewBox="0 0 24 24" aria-hidden="true">
      <path d="M6.6 10.8c1.4 2.8 3.8 5.1 6.6 6.6l2.2-2.2c.3-.3.7-.4 1-.2 1.1.4 2.3.6 3.6.6.6 0 1 .4 1 1V20c0 .6-.4 1-1 1C10.6 21 3 13.4 3 4c0-.6.4-1 1-1h3.5c.6 0 1 .4 1 1 0 1.3.2 2.5.6 3.6.1.3 0 .7-.2 1l-2.3 2.2z" fill="none" stroke="var(--white)" stroke-width="1.6"/>
    </svg>
    <span>0171/5550182</span>
  </div>
  <div class="email">merle.soltau@webpost.de</div>
</main>
</body>
</html>
```